Webdesign für die Veranstaltungsreihe Wolkenreigen
Zielgruppe
Für die Veranstaltungsreihe 'Wolkenreigen' soll ein Website-Design entwickelt werden, welches potentielle Besucher über die Veranstaltung informiert (Standorte, Anfahrt, Preise etc.) und gleichzeitig eine Foto- bzw. Videodokumentation der vergangenen 'Wolkenreigen' bietet.
Zielgruppe:
Personen jeder Altersgruppe, Gruppen wie (Familien, Vereine etc.)
Aufgabenstellung
Das Design sollte...
einfach und modern
nicht zu verspielt
freundlich
kreativ
innovativ
den Inhalt der Veranstaltungsreihe
...wiederspiegeln.
Bitte orientieren Sie sich an dem bestehenden Design der Eventreihe.

```html
<!DOCTYPE html>
<html lang="de">
<head>
<meta charset="utf-8">
<title>Wolkenreigen – Eichenfeld</title>
<link href="https://fonts.googleapis.com/css2?family=Fira+Sans:ital,wght@0,300;0,400;0,500;0,700;1,500;1,700&display=swap" rel="stylesheet">
<style>
:root{
  --dark:#1b1a18;
  --dark-2:#2a2620;
  --gold:#f7b334;
  --gold-light:#fcd36a;
  --gold-deep:#f0a51f;
  --text:#2b2b2b;
  --white:#ffffff;
}
*{margin:0;padding:0;box-sizing:border-box}
html,body{width:880px;height:1200px;overflow:hidden;background:var(--white)}
body{position:relative;font-family:"Fira Sans",sans-serif;color:var(--text)}
.abs{position:absolute}

/* header */
.site-header{left:0;top:0;width:880px;height:105px;background:radial-gradient(ellipse at 15% 40%,#5a4220 0%,transparent 45%),radial-gradient(ellipse at 88% 35%,#5a4220 0%,transparent 45%),var(--dark)}
.header-item{display:flex;align-items:center;gap:8px;color:var(--white);font-size:7px;line-height:8.3px}
.header-item b{font-weight:700}
.icon-box{width:20px;height:20px;display:flex;align-items:center;justify-content:center}
.logo{left:300px;top:26px;width:280px;text-align:center}
.logo-name{font-size:33px;font-weight:700;color:var(--gold);line-height:36px;letter-spacing:-0.5px}
.logo-tag{font-size:11px;font-weight:700;color:var(--white);letter-spacing:.3px;line-height:13px}
.logo-sub{font-size:8px;font-weight:700;color:var(--gold);letter-spacing:.4px;line-height:11px;display:flex;align-items:center;justify-content:center;gap:8px}
.logo-sub::before,.logo-sub::after{content:"";width:22px;height:1px;background:var(--gold)}

/* nav */
.main-nav{left:0;top:105px;width:880px;height:32px;background:linear-gradient(to bottom,var(--gold-light),var(--gold-deep))}
.nav-item{top:0;height:32px;display:flex;align-items:center;justify-content:center;color:var(--white);font-size:9px;border-left:1px solid rgba(160,100,0,.35);text-shadow:0 0 2px rgba(150,90,0,.5)}

/* hero */
.hero{left:0;top:137px;width:880px;height:184px;background:linear-gradient(to bottom,#cfd6dc 0%,#a8b0a8 35%,#7e8a6a 65%,#4f6a33 100%)}
.hero-title{left:0;top:175px;width:880px;text-align:center;color:var(--white);font-weight:700;font-size:33px;line-height:36px;letter-spacing:.5px}
.hero-date{left:0;top:213px;width:880px;text-align:center;color:var(--white);font-weight:300;font-size:26px;line-height:30px}
.hero-btn{left:380px;top:257px;width:120px;height:26px;background:var(--gold);color:var(--white);font-weight:700;font-size:10px;display:flex;align-items:center;justify-content:center}

/* sections */
.section-title{font-size:14px;font-weight:400;color:var(--text)}
.section-title strong{color:var(--gold);font-weight:500}
.intro-media{left:149px;top:368px;width:265px;height:194px;background:radial-gradient(circle at 40% 45%,#8c2a3a 0%,#3a1016 45%,#120608 100%)}
.intro-text{left:414px;top:368px;width:317px;height:194px;background:var(--gold);padding:13px 13px 0 13px;font-size:6.2px;line-height:7.7px;color:#2a1d05}
.intro-text p{margin-bottom:7.7px}
.body-copy{font-size:6.2px;line-height:7.8px;color:var(--text)}
.body-copy p{margin-bottom:7.8px}
.hl{color:var(--gold);font-style:italic;font-weight:700}
.photo{}

/* footer */
.site-footer{left:0;top:1163px;width:880px;height:37px;background:var(--dark)}
.footer-social{left:172px;top:1179px;display:flex;gap:13px}
.footer-social span{width:9px;height:9px;border-radius:50%;background:var(--white);display:block}
.copyright{left:330px;top:1178px;width:216px;text-align:center;color:var(--white);font-size:5.5px;font-weight:700}
.footer-links{left:600px;top:1178px;width:108px;text-align:right;color:var(--white);font-size:5.5px}
</style>
</head>
<body>

<header class="site-header abs">
  <div class="header-item abs" style="left:78px;top:38px">
    <div class="icon-box"><svg width="14" height="14"><rect x="1" y="1" width="12" height="12" fill="var(--gold)"/></svg></div>
    <div>Follow us on<br><b>freundeskreis.net/</b><br><b>Wolkenreigen.de</b></div>
  </div>
  <div class="header-item abs" style="left:188px;top:38px">
    <div class="icon-box"><svg width="22" height="16" viewBox="0 0 22 16"><rect x="2" y="3" width="18" height="10" rx="1" fill="var(--gold)" transform="rotate(-8 11 8)"/><rect x="3" y="6" width="18" height="8" rx="1" fill="var(--gold-deep)"/></svg></div>
    <div>Verfügbare Tickets<br>finden Sie im<br><b>ticketwelt.de - Shop</b></div>
  </div>
  <div class="logo abs">
    <div class="logo-name">WOLKENREIGEN</div>
    <div class="logo-tag">DER WETTSTREIT DER PYROTECHNIKER</div>
    <div class="logo-sub">DREI FANTASTISCHE MUSIKFEUERWERKE</div>
  </div>
  <div class="header-item abs" style="left:594px;top:38px">
    <div class="icon-box"><svg width="14" height="22" viewBox="0 0 14 22"><rect x="1" y="1" width="12" height="20" rx="2" fill="none" stroke="var(--gold)" stroke-width="2"/><rect x="3" y="4" width="8" height="12" fill="var(--gold)"/><circle cx="7" cy="18.5" r="1" fill="var(--gold)"/></svg></div>
    <div>Unsere Service<br>HOTLINE<br><b>(02 09) 555 01 234</b></div>
  </div>
  <div class="header-item abs" style="left:719px;top:38px">
    <div class="icon-box"><svg width="22" height="22"><rect x="1" y="1" width="20" height="20" rx="3" fill="var(--gold)"/></svg></div>
    <div>Follow us on<br><b>bildstrom.net/</b><br><b>wolkenreigen</b></div>
  </div>
</header>

<nav class="main-nav abs">
  <div class="nav-item abs" style="left:173px;width:97px">Home</div>
  <div class="nav-item abs" style="left:270px;width:98px">Standorte</div>
  <div class="nav-item abs" style="left:368px;width:116px">Tickets &amp; Preise</div>
  <div class="nav-item abs" style="left:484px;width:116px">Fotos &amp; Videos</div>
  <div class="nav-item abs" style="left:600px;width:108px;border-right:1px solid rgba(160,100,0,.35)">FAQ / Regeln</div>
</nav>

<section class="hero abs" role="img" aria-label="Foto: Schloss mit Park, Festzelten und Springbrunnen"></section>
<h1 class="hero-title abs">EICHENFELD</h1>
<div class="hero-date abs">13. AUGUST 2016 - SCHLOSSPARK LINDENAU</div>
<div class="hero-btn abs">TICKETS KAUFEN!</div>

<h2 class="section-title abs" style="left:149px;top:343px"><strong>Was ist</strong> Wolkenreigen?</h2>
<div class="intro-media abs" role="img" aria-label="Video: Feuerwerk in Rot und Grün über einem Schloss">
  <svg class="abs" style="left:90px;top:55px" width="86" height="86" viewBox="0 0 86 86"><circle cx="43" cy="43" r="40" fill="none" stroke="#fff" stroke-width="3"/><path d="M32 24 L62 43 L32 62 Z" fill="none" stroke="#fff" stroke-width="3" stroke-linejoin="round"/></svg>
</div>
<div class="intro-text abs">
  <p>Wolkenreigen - Der Wettstreit der Pyrotechniker mit drei fantastischen Musikfeuerwerken<br>Drei renommierte Pyrotechniker treten beim Wolkenreigen gegeneinander an und versuchen, das Publikum und die Fachjury mit ihren spektakulären Feuerwerks-Choreografien zu überzeugen und den Siegerpokal für sich zu gewinnen.</p>
  <p>Das ist was ganz besonderes: die Feuerwerks-Künstler sind frei in Ihrer künstlerischen Gestaltung, zu ihrem selbst ausgewählten musikalischen Thema kreieren sie mit ihrer ganz eigenen Handschrift ein Gesamtkunstwerk. Neben der passenden Farb- und Effektauswahl kommt es besonders darauf an, dass Sterne, Kometen und Lichtblitze auf die Zehntelsekunde genau im Takt der Musik am Himmel erscheinen - ein Genuss für Augen und Ohren! Neben beeindruckenden und bombastischen Feuerblumen am Himmel, wie rauschenden Sternschnuppen oder funkelndem Goldregen, können die Teams mit ausgefallenen und seltenen Bodenfeuerwerks-Elementen, wie kleinen und großen Feuerrädern, Wasserfällen und Springbrunnen aus Feuer punkten.</p>
  <p>Jedes Team hat bis zu 15 Minuten Zeit, die Zuschauer zu beeindrucken und sich den Sieg zu sichern. Doch bevor die Feuerwerks-Künstler in ihrer Kür zeigen was sie können, müssen sie ihre Effekte zunächst in einem ca. 2 Minuten langen Pflichtteil arrangieren, um die verschiedenen Ideen und Stile der Teilnehmer besser vergleichen zu können.</p>
  <p>Bevor die fantastischen Musikfeuerwerke den Park und den Himmel erleuchten, runden ein Rahmenprogramm für die ganze Familie und ein großes kulinarisches Angebot den Abend stimmig ab - <b><i>lassen Sie sich verzaubern!</i></b></p>
</div>

<h2 class="section-title abs" style="left:149px;top:586px"><strong>Ein abwechslungsreiches</strong> Rahmenprogramm:</h2>

<div class="body-copy abs" style="left:167px;top:623px;width:334px">
  <p>Ab Einlassbeginn um 17:00 Uhr begrüßt die <span class="hl">Samba-Gruppe Batucada aus Hagenfeld</span> die Besucher mit heißen Rhythmen. Sie spielen ein breites Spektrum brasilianischer Rhythmus-Kultur. Modernes, Traditionelles, Schnelles, Langsames, Melodiöses und Percussives sorgen für ein abwechslungreiches Programm. Hingucker und Ohrenschmaus in Einem!</p>
</div>
<div class="photo abs" style="left:524px;top:610px;width:206px;height:137px;background:linear-gradient(to bottom,#8fb6e0 0%,#a9c3cf 40%,#5d7a3e 70%,#8a8a80 100%)" role="img" aria-label="Foto: Sambagruppe in bunten Kostümen auf einem Parkweg"></div>

<div class="photo abs" style="left:149px;top:670px;width:122px;height:175px;background:linear-gradient(to bottom,#d6d6d6,#a9a9a9)" role="img" aria-label="Foto: DJ in Jeanshemd, schwarz-weiß"></div>
<div class="body-copy abs" style="left:289px;top:683px;width:212px">
  <p>NEU in diesem Jahr: <span class="hl">Die ChillOut-Area!</span> In der ChillOut-Area sorgt der niederländische <span class="hl">Top-DJ Tom Tessen</span> (Foto) den ganzen Abend über für coole Beats. Er ist Experte auf den Bereichen Deep House, Tech House und ChillOut-Classics und bekannter Resident-DJ zahlreicher niederländischer Clubs. Mit Cocktails, Beach-Volleyball, Tischtennis und Basketball kommt garantiert keine Langeweile auf, während der Sommer genossen und in den warmen Sonnenstrahlen gechillt werden kann.</p>
</div>
<div class="photo abs" style="left:289px;top:747px;width:172px;height:98px;background:radial-gradient(ellipse at 65% 45%,#b27a3c 0%,#4a2c12 55%,#1a0f06 100%)" role="img" aria-label="Foto: Akustik-Duo mit Gitarre und Mikrofon"></div>
<div class="body-copy abs" style="left:483px;top:767px;width:234px">
  <p>Ab 18:00 Uhr beginnt das Rahmenprogramm mit <span class="hl">Lenni und Mika</span>. Eine Akustikgitarre, gefühlvoller Gesang, eine akustische Bass-Gitarre und würzige Percussion - das sind Lenni und Mika. Mit Ihrem selbstgeschriebenen Akustik-Pop erobert das junge Duo gerade die Bretter der Welt.</p>
  <p>Das Repertoire reicht dabei von sensiblen und emotionalen Balladen bis hin zu schnellen und rockigen Stücken - angereichert mit viel Witz und Charme nehmen sie ihre Zuhörer mit auf eine kleine Reise hinaus aus dem Alltag.</p>
</div>

<div class="body-copy abs" style="left:166px;top:857px;width:308px">
  <p>Danach übernimmt <span class="hl">die Lindener Coverband Volltakt</span> (Foto). Die sechs (mehr oder weniger) jungen Musiker haben eine überzeugende Mischung aus Klassikern, Party-Classics und aktuellen Hits im Repertoire, denen sie immer einen eigenen Stempel aufdrücken und mit voller Begeisterung auf die Bühne bringen.</p>
  <p>Mit viel Spaß an der Musik und Interaktion mit dem Publikum rocken sie auf der Bühne ab und bringen jede Party zum Kochen. Eins ist auf jeden Fall klar: Sie freuen sich darauf, ihr Publikum mit guter, handgemachter Musik vom ersten Ton an mitzureißen.</p>
</div>
<div class="photo abs" style="left:496px;top:845px;width:235px;height:159px;background:radial-gradient(ellipse at 50% 55%,#7a4a24 0%,#2a160a 60%,#0c0604 100%)" role="img" aria-label="Foto: Coverband live auf der Bühne"></div>

<div class="photo abs" style="left:149px;top:931px;width:183px;height:223px;background:radial-gradient(ellipse at 50% 50%,#5a2a10 0%,#1a0a04 60%,#050202 100%)" role="img" aria-label="Foto: Feuerkünstlerinnen mit brennenden Fächern"></div>
<div class="body-copy abs" style="left:347px;top:931px;width:140px">
  <p><span class="hl">Die Flammenschwestern</span>, ein Artistinnen-Trio, sorgen gegen Einbruch der Dunkelheit für stockenden Atem: Sie verstehen es mit dem Feuer zu spielen! Sie bieten eine explosive, heiße Show, in der Tanz, Feuerjonglage und Pyroeffekte miteinander vereint werden.</p>
  <p>Die Flammenschwestern sind bekannt für ihre einzigartigen Shows, mit denen Sie bereits weltweit aufgetreten sind. Mit ihrer faszinierender Feuerartistik sorgen die Flammenschwestern für die ideale Einstimmung auf die Feuerwerke.</p>
</div>
<div class="body-copy abs" style="left:347px;top:1039px;width:370px">
  <p>Auch für die jüngeren Gäste ist gesorgt: Für sie wird es wieder eine <span class="hl">kostenfreie Kinderspielinsel</span> mit verschiedensten Spiele- und Spaßelementen geben. Außerdem dabei: Bungee-Trampolin, Bull-Riding und Hüpfburg.</p>
  <p><span class="hl">Feuerspucker</span> als Walk-Acts auf dem Gelände begrüßen die Besucher mit Feuerjonglage und kleinen Feuerspuckeinlagen. Abgerundet wird der Abend durch ein in diesem Jahr <span class="hl">noch größeres und vielfältigeres kulinarisches Angebot</span>: Von der klassischen Rostbratwurst über Pfannengerichte bis hin zu Flammlachs ist alles mit dabei, neben den klassischen Getränken kommen auch Cocktail- und Weinliebhaber nicht zu kurz.</p>
  <p>Moderierend durch den Abend führt die bekannte Stimme <span class="hl">Ralf Berendt</span>.</p>
</div>

<footer class="site-footer abs"></footer>
<div class="footer-social abs"><span></span><span></span><span></span><span></span><span></span><span></span></div>
<div class="copyright abs">COPYRIGHT 2016. ALL RIGHTS RESERVED</div>
<div class="footer-links abs">FAQ &nbsp;|&nbsp; AGB &nbsp;|&nbsp; IMPRESSUM &nbsp;|&nbsp; KONTAKT</div>

</body>
</html>
```